New Business Card Design Project

Hi,

I'd like to create a logo for my business www.tansyandloom.example. You will need to download two fonts for the business card: Lobster & Noticia Text. The fonts are free to download. No logo required.

Potential design idea:
One side hot pink (white font), one side white (grey font)
- On one side, hot pink similar to the pink on the website.
- Show tansy + loom plus "your ever-turning wardrobe" in white font
- We really need it to be sleek, minimalistic and bright
- On the other side, we need to show our instagram and facebook URLs (friendly.example/tansyandloom, snapgrid.example/tansyandloom). Please use the same dark grey font as our website and use a hollowed out grey FB & Instagram logo
We also need to show the following details, website, space for name and email (hello@tansyandloom.example).

Feel free to go as creative as you would like! The above is a safe template that we know will satisfy our needs. Aim is to minimalist, simple and bold. , Details for my new Business Card Design Project will be added soon.

Industry/Entity Type

Business

Font styles to use
Sans Serif

Requirements
Must have
• Needs to fit the quillprint.example luxe business card template.

```html
<!DOCTYPE html>
<html lang="en">
<head>
<meta charset="utf-8">
<title>tansy + loom business card</title>
<link rel="stylesheet" href="https://fonts.googleapis.com/css2?family=Lobster&family=Noticia+Text:wght@400;700&display=swap">
<style>
  :root {
    --backdrop: #e6e6e6;
    --hot-pink: #f06478;
    --card-white: #ffffff;
    --ink-white: #ffffff;
    --ink-grey: #555555;
    --name-grey: #666666;
  }
  * { margin: 0; padding: 0; box-sizing: border-box; }
  html, body { width: 1200px; height: 1000px; overflow: hidden; }
  body {
    background: var(--backdrop);
    position: relative;
    font-family: "Noticia Text", Georgia, serif;
  }
  .card {
    position: absolute;
    left: 233px;
    width: 734px;
    height: 420px;
  }
  .card--front { top: 45px; background: var(--hot-pink); }
  .card--back { top: 535px; background: var(--card-white); color: var(--ink-grey); }

  .brand-mark {
    position: absolute;
    left: 29px;
    top: 142px;
    width: 123px;
    height: 123px;
    border: 5px solid var(--ink-white);
    display: flex;
    align-items: center;
    justify-content: center;
    color: var(--ink-white);
    font-family: "Noticia Text", Georgia, serif;
    font-weight: 700;
    font-size: 19px;
    text-align: center;
    line-height: 1.25;
  }
  .tagline {
    position: absolute;
    left: 182px;
    top: 170px;
    color: var(--ink-white);
    font-family: "Lobster", cursive;
    font-size: 50px;
    line-height: 1;
    white-space: nowrap;
  }

  .social-list {
    position: absolute;
    left: 38px;
    top: 33px;
    list-style: none;
  }
  .social-list li {
    display: flex;
    align-items: center;
    height: 44px;
    font-size: 26px;
  }
  .social-icon { width: 28px; height: 28px; margin-right: 16px; flex: none; }

  .holder-name {
    position: absolute;
    left: 0;
    right: 0;
    top: 188px;
    text-align: center;
    font-family: "Lobster", cursive;
    font-size: 68px;
    letter-spacing: 4px;
    color: var(--name-grey);
    line-height: 1;
  }
  .contact-lines {
    position: absolute;
    right: 26px;
    top: 320px;
    text-align: right;
    font-size: 26px;
    line-height: 37px;
  }
</style>
</head>
<body>
  <section class="card card--front">
    <div class="brand-mark">tansy<br>+ loom</div>
    <p class="tagline">your ever-turning wardrobe</p>
  </section>

  <section class="card card--back">
    <ul class="social-list">
      <li>
        <svg class="social-icon" viewBox="0 0 28 28" aria-hidden="true">
          <rect x="1.5" y="1.5" width="25" height="25" rx="4" fill="none" stroke="#555555" stroke-width="2"/>
        </svg>
        friendly.example/tansyandloom
      </li>
      <li>
        <svg class="social-icon" viewBox="0 0 28 28" aria-hidden="true">
          <rect x="1.5" y="1.5" width="25" height="25" rx="4" fill="none" stroke="#555555" stroke-width="2"/>
        </svg>
        snapgrid.example/tansyandloom
      </li>
    </ul>

    <p class="holder-name">Mirela Oduya</p>

    <p class="contact-lines">
      www.tansyandloom.example<br>
      hello@tansyandloom.example
    </p>
  </section>
</body>
</html>
```